NEW Business Cards!
CNC Machine Shop Business Cards
Simple
Dale Workman
248 North Route 371
Kelvale, Texas 75418
WorkmanIronCraft@mailbox-example.com
www.WorkmanIronCraft.example
We also need this person on the same card somehow:
Travis Workman
Cell - 555.218.7730
Fax - Same
email - Same
In-House Services:
CNC Milling
CNC Turning
CNC Bending
Water Jet Cutting
Powder Coating

```html
<!DOCTYPE html>
<html lang="en">
<head>
<meta charset="utf-8">
<title>Workman Metal Works – Business Cards</title>
<link href="https://fonts.googleapis.com/css2?family=Russo+One&family=Roboto:wght@400;500;700&display=swap" rel="stylesheet">
<style>
  :root {
    --backdrop: #5e4129;
    --card-white: #f8f8f8;
    --card-shade: #e4e4e4;
    --gold-light: #d9c49c;
    --gold-mid: #a98b5c;
    --gold-dark: #6f5634;
    --brand-blue: #1d5fa8;
    --rule-blue: #2a7fd0;
    --name-gold: #8a6b3c;
    --ink: #1f1f1f;
    --ink-soft: #2c2c2c;
  }
  * { box-sizing: border-box; margin: 0; padding: 0; }
  html, body { width: 1200px; height: 969px; overflow: hidden; }
  body {
    background: var(--backdrop);
    position: relative;
    font-family: "Roboto", Arial, sans-serif;
  }
  .card {
    position: absolute;
    top: 165px;
    width: 384px;
    height: 668px;
    border-radius: 30px;
    overflow: hidden;
    background: linear-gradient(180deg, var(--card-white) 0%, var(--card-shade) 100%);
    box-shadow: 0 6px 18px rgba(0,0,0,0.35);
  }
  .card--front { left: 173px; }
  .card--back { left: 645px; }

  .card__base {
    position: absolute;
    left: 0; right: 0; bottom: 0;
    height: 253px;
    background: linear-gradient(180deg, var(--gold-light) 0%, var(--gold-mid) 45%, var(--gold-dark) 100%);
  }
  .card__base::before {
    content: "";
    position: absolute;
    left: 0; right: 0; top: -9px;
    height: 4px;
    background: var(--rule-blue);
  }
  .card__base::after {
    content: "";
    position: absolute;
    left: 0; right: 0; top: -5px;
    height: 5px;
    background: #ffffff;
  }

  .contact__name,
  .contact__phone { position: absolute; left: 0; right: 0; }
  .contact__name {
    text-align: center;
    font-family: "Russo One", Arial, sans-serif;
    font-size: 24px;
    color: var(--name-gold);
    text-transform: uppercase;
    line-height: 1;
  }
  .contact__phone {
    text-align: right;
    padding-right: 44px;
    font-family: "Roboto", Arial, sans-serif;
    font-weight: 500;
    font-size: 19px;
    color: var(--ink-soft);
    line-height: 1;
  }
  .contact__name--first { top: 22px; }
  .contact__phone--first { top: 56px; }
  .contact__name--second { top: 90px; }
  .contact__phone--second { top: 124px; }

  .brand__mark {
    position: absolute;
    left: 50%;
    background: var(--brand-blue);
  }
  .card--front .brand__mark { top: 190px; width: 96px; height: 96px; margin-left: -48px; }
  .card--back .brand__mark { top: 96px; width: 140px; height: 140px; margin-left: -70px; }

  .brand__name,
  .brand__sub {
    position: absolute;
    left: 0; right: 0;
    text-align: center;
    font-family: "Russo One", Arial, sans-serif;
    color: var(--brand-blue);
    text-transform: uppercase;
    line-height: 1;
  }
  .card--front .brand__name { top: 328px; font-size: 38px; }
  .card--front .brand__sub { top: 374px; font-size: 16px; letter-spacing: 5px; }
  .card--back .brand__name { top: 282px; font-size: 44px; }
  .card--back .brand__sub { top: 334px; font-size: 18px; letter-spacing: 6px; }

  .address {
    position: absolute;
    top: 464px;
    left: 102px;
    font-size: 16px;
    color: var(--ink);
    line-height: 26px;
  }
  .address__fax { margin-top: 14px; }
  .web {
    position: absolute;
    top: 572px;
    left: 16px;
    font-size: 14px;
    color: var(--ink);
    line-height: 26px;
  }

  .services {
    position: absolute;
    top: 424px;
    left: 40px;
  }
  .services__title {
    font-weight: 500;
    font-size: 26px;
    color: var(--ink);
    line-height: 34px;
    margin-bottom: 4px;
  }
  .services__list { list-style: none; }
  .services__item {
    display: flex;
    align-items: center;
    font-size: 23px;
    font-weight: 500;
    color: var(--ink);
    line-height: 37px;
  }
  .services__icon { width: 20px; height: 20px; margin-right: 12px; flex: none; }
</style>
</head>
<body>

  <section class="card card--front" aria-label="Card front">
    <div class="card__base"></div>

    <p class="contact__name contact__name--first">Dale Workman</p>
    <p class="contact__phone contact__phone--first">C : 555.304.1182</p>
    <p class="contact__name contact__name--second">Travis Workman</p>
    <p class="contact__phone contact__phone--second">C : 555.218.7730</p>

    <span class="brand__mark"></span>
    <p class="brand__name">Workman</p>
    <p class="brand__sub">Metal Works</p>

    <div class="address">
      <p>248 North Route 371</p>
      <p>Kelvale, Texas 75418</p>
      <p class="address__fax">F : 555.607.2291</p>
    </div>

    <div class="web">
      <p>E : WorkmanIronCraft@mailbox-example.com</p>
      <p>W : www.WorkmanIronCraft.example</p>
    </div>
  </section>

  <section class="card card--back" aria-label="Card back">
    <div class="card__base"></div>

    <span class="brand__mark"></span>
    <p class="brand__name">Workman</p>
    <p class="brand__sub">Metal Works</p>

    <div class="services">
      <p class="services__title">In-House Services</p>
      <ul class="services__list">
        <li class="services__item"><svg class="services__icon" viewBox="0 0 22 22" aria-hidden="true"><circle cx="11" cy="11" r="10" fill="#2a7fd0"/><path d="M8 6 L15 11 L8 16 Z" fill="#ffffff"/></svg>CNC Milling</li>
        <li class="services__item"><svg class="services__icon" viewBox="0 0 22 22" aria-hidden="true"><circle cx="11" cy="11" r="10" fill="#2a7fd0"/><path d="M8 6 L15 11 L8 16 Z" fill="#ffffff"/></svg>CNC Turning</li>
        <li class="services__item"><svg class="services__icon" viewBox="0 0 22 22" aria-hidden="true"><circle cx="11" cy="11" r="10" fill="#2a7fd0"/><path d="M8 6 L15 11 L8 16 Z" fill="#ffffff"/></svg>CNC Bending</li>
        <li class="services__item"><svg class="services__icon" viewBox="0 0 22 22" aria-hidden="true"><circle cx="11" cy="11" r="10" fill="#2a7fd0"/><path d="M8 6 L15 11 L8 16 Z" fill="#ffffff"/></svg>Water Jet Cutting</li>
        <li class="services__item"><svg class="services__icon" viewBox="0 0 22 22" aria-hidden="true"><circle cx="11" cy="11" r="10" fill="#2a7fd0"/><path d="M8 6 L15 11 L8 16 Z" fill="#ffffff"/></svg>Powder Coating</li>
      </ul>
    </div>
  </section>

</body>
</html>
```